Brightmoor Senior Living Marketing Brochure, Covid-19 Brochure, Introduction to our manager

We are a Senior Living Community that services Assisted living and memory care. We have a lot of New programs for Activities, Food recipes, therapy, family and resident interaction , covid free, and want to introduce this to the community and existing family members.

Target Market(s)

La Jolla and San Diego for Brightmoor Senior Living and Memory Care of La Jolla and For Brightmoor Senior Living and Memory Care of Tarzana , San Fernando valley, tarzana, Encino , Woodland Hills Sherman oaks

Industry/Entity Type

Assisted Living

Font styles to use
Other font styles liked:
• TBD

Colors
a54499
f7f3f9
ffffff
fece3e
ffc214

Requirements
Must have
• Product names for our marketing brochure , facility images per location

```html
<!DOCTYPE html>
<html lang="en">
<head>
<meta charset="utf-8">
<title>Brightmoor Senior Living – Brochure</title>
<link href="https://fonts.googleapis.com/css2?family=Montserrat:wght@400;500;600;700&family=Saira+Condensed:wght@200;300;400&display=swap" rel="stylesheet">
<style>
  :root {
    --magenta: #a54499;
    --magenta-deep: #c0137f;
    --magenta-bright: #d83fb0;
    --lilac: #f7f3f9;
    --white: #ffffff;
    --gold: #fece3e;
    --gold-deep: #ffc214;
    --gold-text: #d8ae2c;
    --ink: #2b2b2b;
    --backdrop: #d3d7d9;
  }
  * { box-sizing: border-box; margin: 0; padding: 0; }
  html, body { width: 913px; height: 1200px; overflow: hidden; }
  body { background: var(--backdrop); font-family: "Montserrat", sans-serif; color: var(--ink); }

  .spread {
    position: absolute; left: 66px; width: 780px; height: 551px; overflow: hidden;
    background: var(--white); box-shadow: 0 6px 18px rgba(0,0,0,.18);
  }
  .spread--cover { top: 36px; }
  .spread--inner { top: 613px; }
  .spread__art { position: absolute; inset: 0; width: 780px; height: 551px; }

  /* back cover */
  .back-contact { position: absolute; left: 34px; bottom: 16px; color: var(--white); font-size: 8.5px; line-height: 1.55; }
  .brand-name { font-family: "Montserrat", sans-serif; font-weight: 600; letter-spacing: .12em; }
  .back-contact .brand-name { font-size: 15px; color: var(--white); }
  .brand-tag { font-size: 6px; letter-spacing: .14em; text-transform: uppercase; margin-bottom: 8px; }
  .back-contact .city { font-weight: 700; letter-spacing: .04em; margin-top: 3px; }
  .contact-line { display: flex; align-items: center; gap: 5px; }
  .contact-line svg { width: 8px; height: 8px; flex: none; }
  .follow { display: flex; align-items: center; gap: 5px; margin-top: 5px; }
  .follow span.dot { width: 9px; height: 9px; border-radius: 50%; background: var(--gold); display: inline-block; }

  /* front cover */
  .front-title { position: absolute; left: 515px; top: 196px; width: 245px; text-align: right; }
  .front-title .brand-name { color: var(--gold-text); font-size: 16px; }
  .front-title .brand-tag { color: var(--gold-text); font-size: 5.5px; margin-bottom: 4px; }
  .front-title .line { font-family: "Saira Condensed", sans-serif; line-height: .95; text-transform: uppercase; white-space: nowrap; }
  .line--light { font-weight: 200; font-size: 32px; color: var(--gold-text); }
  .line--strong { font-weight: 300; font-size: 42px; color: var(--magenta-deep); }
  .url-pill {
    display: inline-block; margin-top: 10px; padding: 3px 12px; border-radius: 10px;
    background: var(--magenta-bright); color: var(--white); font-size: 8.5px; font-weight: 600;
  }

  /* inner spread */
  .inner-copy { position: absolute; left: 430px; top: 36px; width: 320px; }
  .intro { color: var(--magenta-deep); font-size: 10.5px; line-height: 1.4; }
  .section-head { display: flex; align-items: center; gap: 8px; margin: 14px 0 8px; color: var(--magenta-deep); font-size: 17px; font-weight: 400; text-transform: uppercase; }
  .section-head::after { content: ""; flex: 1; height: 1px; background: var(--magenta-bright); }
  .care-option { display: grid; grid-template-columns: 24px 1fr; gap: 0 6px; margin-bottom: 8px; }
  .care-option__icon { width: 22px; height: 22px; border-radius: 50%; background: var(--gold); border: 2px solid var(--white); box-shadow: 0 0 0 1px var(--gold); display: flex; align-items: center; justify-content: center; }
  .care-option__icon i { width: 9px; height: 9px; border-radius: 50%; background: var(--magenta-deep); }
  .care-option__label { align-self: center; justify-self: start; background: var(--gold-deep); color: var(--white); font-size: 9px; font-weight: 700; padding: 3px 12px; border-radius: 0 10px 10px 0; }
  .care-option p { grid-column: 2; font-size: 7.5px; font-weight: 500; line-height: 1.4; margin-top: 3px; }
  .programs { display: flex; justify-content: space-between; text-align: center; }
  .program { width: 62px; font-size: 8px; color: var(--ink); }
  .program__icon { width: 32px; height: 32px; margin: 0 auto 4px; border-radius: 50%; background: var(--gold); border: 3px solid var(--white); box-shadow: 0 0 0 1px var(--gold); display: flex; align-items: center; justify-content: center; }
  .program__icon i { width: 14px; height: 14px; border-radius: 3px; background: var(--magenta-bright); }
</style>
</head>
<body>

<section class="spread spread--cover" aria-label="Brochure cover spread">
  <svg class="spread__art" viewBox="0 0 780 551" aria-hidden="true">
    <defs>
      <linearGradient id="backGrad" x1="0" y1="0" x2="1" y2="1">
        <stop offset="0" stop-color="#a54499"/>
        <stop offset=".6" stop-color="#c0137f"/>
        <stop offset="1" stop-color="#b01079"/>
      </linearGradient>
      <linearGradient id="swoosh" x1="0" y1="0" x2="1" y2="1">
        <stop offset="0" stop-color="#b81a86"/>
        <stop offset="1" stop-color="#e46ad0"/>
      </linearGradient>
    </defs>
    <rect x="0" y="0" width="390" height="551" fill="url(#backGrad)"/>
    <rect x="390" y="0" width="390" height="551" fill="#fbfafb"/>
    <!-- magenta band sweeping from the spine under the photo circle -->
    <path d="M390 290 C 470 285, 560 290, 640 310 C 560 330, 500 380, 500 440 C 500 500, 560 540, 620 551 L 390 551 Z" fill="url(#swoosh)"/>
    <!-- gold arc bordering the band on the back cover -->
    <path d="M392 292 C 350 320, 340 400, 380 460 C 420 510, 470 535, 520 551" fill="none" stroke="var(--gold)" stroke-width="7"/>
    <circle cx="475" cy="105" r="205" fill="var(--gold)"/>
    <circle cx="475" cy="105" r="195" fill="var(--white)"/>
  </svg>
  <svg class="spread__art" viewBox="0 0 780 551" role="img" aria-label="Photograph of a grandfather and young grandson sharing a warm moment in golden light">
    <defs>
      <radialGradient id="photoWarm" cx=".6" cy=".4" r=".7">
        <stop offset="0" stop-color="#f2c98a"/>
        <stop offset=".5" stop-color="#b77b45"/>
        <stop offset="1" stop-color="#4a2f1e"/>
      </radialGradient>
    </defs>
    <circle cx="475" cy="105" r="185" fill="url(#photoWarm)"/>
  </svg>

  <div class="back-contact">
    <div class="brand-name">BRIGHTMOOR</div>
    <div class="brand-tag">Senior Living &amp; Memory Care</div>
    <div class="city">TARZANA, CALIFORNIA</div>
    <div class="contact-line"><svg viewBox="0 0 10 10"><path d="M2 1 L4 1 L5 3 L4 4 C4.5 5.5 5 6 6 6 L7 5 L9 6 L9 8 C5 9 1 5 2 1 Z" fill="var(--gold)"/></svg>(818) 555-0142</div>
    <div class="contact-line"><svg viewBox="0 0 10 10"><path d="M5 0.5 C2.8 0.5 1.5 2 1.5 4 C1.5 6.5 5 9.5 5 9.5 C5 9.5 8.5 6.5 8.5 4 C8.5 2 7.2 0.5 5 0.5 Z" fill="var(--gold)"/><circle cx="5" cy="4" r="1.3" fill="var(--magenta)"/></svg>1820 Cedarline Avenue, Tarzana, CA 91356</div>
    <div class="city">LA JOLLA, CALIFORNIA</div>
    <div class="contact-line"><svg viewBox="0 0 10 10"><path d="M2 1 L4 1 L5 3 L4 4 C4.5 5.5 5 6 6 6 L7 5 L9 6 L9 8 C5 9 1 5 2 1 Z" fill="var(--gold)"/></svg>(858) 555-0176</div>
    <div class="contact-line"><svg viewBox="0 0 10 10"><path d="M5 0.5 C2.8 0.5 1.5 2 1.5 4 C1.5 6.5 5 9.5 5 9.5 C5 9.5 8.5 6.5 8.5 4 C8.5 2 7.2 0.5 5 0.5 Z" fill="var(--gold)"/><circle cx="5" cy="4" r="1.3" fill="var(--magenta)"/></svg>1820 Cedarline Avenue, Tarzana, CA 91356</div>
    <div class="contact-line"><svg viewBox="0 0 10 10"><circle cx="5" cy="5" r="4" fill="var(--gold)"/></svg>www.brightmoorseniorliving.com</div>
    <div class="follow">Follow us on <span class="dot"></span><span class="dot"></span><span class="dot"></span><span class="dot"></span></div>
  </div>

  <div class="front-title">
    <div class="brand-name">BRIGHTMOOR</div>
    <div class="brand-tag">Senior Living &amp; Memory Care</div>
    <div class="line line--light">A Luxurious</div>
    <div class="line line--strong">Senior Living</div>
    <div class="line line--light">Community</div>
    <span class="url-pill">www.brightmoorseniorliving.com</span>
  </div>
</section>

<section class="spread spread--inner" aria-label="Brochure inside spread">
  <svg class="spread__art" viewBox="0 0 780 551" aria-hidden="true">
    <defs>
      <linearGradient id="innerSwoosh" x1="0" y1="0" x2="1" y2="0">
        <stop offset="0" stop-color="#b81a86"/>
        <stop offset="1" stop-color="#e46ad0"/>
      </linearGradient>
    </defs>
    <rect x="390" y="0" width="390" height="551" fill="var(--lilac)"/>
    <path d="M0 0 L300 0 C 380 60, 410 200, 330 270 C 410 340, 400 480, 360 551 L0 551 Z" fill="url(#innerSwoosh)"/>
  </svg>
  <svg class="spread__art" viewBox="0 0 780 551" role="img" aria-label="Photographs of the two community buildings: a garden entrance with signage and a modern lit entryway at dusk">
    <defs>
      <linearGradient id="bldgDay" x1="0" y1="0" x2="0" y2="1">
        <stop offset="0" stop-color="#3f6fc4"/>
        <stop offset=".45" stop-color="#c9ad86"/>
        <stop offset="1" stop-color="#8a7a56"/>
      </linearGradient>
      <linearGradient id="bldgDusk" x1="0" y1="0" x2="0" y2="1">
        <stop offset="0" stop-color="#e8e4e0"/>
        <stop offset=".55" stop-color="#9b7a4e"/>
        <stop offset="1" stop-color="#e3a53f"/>
      </linearGradient>
    </defs>
    <path d="M0 0 L285 0 C 355 60, 380 190, 315 262 L0 262 Z" fill="url(#bldgDay)"/>
    <path d="M0 276 L318 276 C 385 350, 380 480, 345 551 L0 551 Z" fill="url(#bldgDusk)"/>
  </svg>

  <div class="inner-copy">
    <p class="intro">At Brightmoor, we know that each senior who comes through our doors has a unique set of interests &amp; needs. We provide living arrangements that suit your lifestyle with various levels of care &amp; personal assistance.</p>

    <h2 class="section-head">Our Caer Options</h2>
    <div class="care-option">
      <span class="care-option__icon"><i></i></span>
      <span class="care-option__label">Independent Living</span>
      <p>Our independent living community provides older adults with everything they need to maintain their independence as they age.</p>
    </div>
    <div class="care-option">
      <span class="care-option__icon"><i></i></span>
      <span class="care-option__label">Assisted Care</span>
      <p>At Brightmoor Senior Living and Memory Care the outstanding, comprehensive, licensed assisted living program is the hallmark of our service.</p>
    </div>
    <div class="care-option">
      <span class="care-option__icon"><i></i></span>
      <span class="care-option__label">Memory Care</span>
      <p>At Brightmoor Senior Living and Memory Care, our caregivers give residents and their families the support they need for living with memory loss.</p>
    </div>

    <h2 class="section-head">Our New Programs</h2>
    <div class="programs">
      <div class="program"><div class="program__icon"><i></i></div>Activities</div>
      <div class="program"><div class="program__icon"><i></i></div>Food recipes</div>
      <div class="program"><div class="program__icon"><i></i></div>Therapy</div>
      <div class="program"><div class="program__icon"><i></i></div>Family &amp; Resident Interaction</div>
      <div class="program"><div class="program__icon"><i></i></div>Covid Free</div>
    </div>
  </div>
</section>

</body>
</html>
```